Vorlisk.com Redesign

Please read the notes and see the site-map attached.
Updates

We are looking for something highly creative. Please provide your best work. Best of luck and thank you very much for your hard work!

Project Deadline Extended
Reason: I am seeing good designs but I am not seeing great designs. I really need a design that is unique and is going to wow me. No one is required to stick to the existing color schemes etc. You are free to use other colors etc. I am seeing a lot of the same colors that are used on the site now.

Target Market(s)

Business and entrepreneurs mainly. People looking to build applications, software or launch web or mobile tech products.

Colors

Designer to choose colors to be used in the design.

Requirements
Must have
• See my attached html file.
Nice to have
Should not have
• No sure

```html
<!DOCTYPE html>
<html lang="en">
<head>
<meta charset="utf-8">
<title>Vorlisk</title>
<link rel="stylesheet" href="https://fonts.googleapis.com/css2?family=Ubuntu:ital,wght@0,400;0,500;0,700;1,400&family=Roboto+Condensed:wght@300;400&family=Arimo:wght@400;700&display=swap">
<style>
:root{
  --green:#7cbf43;
  --green-dark:#5d9a2c;
  --ink:#2b3a42;
  --text:#4a4a4a;
  --muted:#666;
  --dark:#1e2326;
  --footer:#ececec;
  --bar:#2a2d30;
  --white:#fff;
}
*{margin:0;padding:0;box-sizing:border-box}
html,body{width:759px;height:1200px;overflow:hidden}
body{position:relative;background:#fbfbfb;font-family:"Ubuntu",sans-serif;color:var(--text)}
.abs{position:absolute}
.hero{left:0;top:0;width:759px;height:358px;background:linear-gradient(100deg,#2c2a26 0%,#3b3a36 45%,#2a2f31 100%)}
.hero-photo{left:80px;top:80px;width:336px;height:278px;background:radial-gradient(ellipse at 40% 50%,#c99a80 0%,#7a5a4c 45%,rgba(40,40,40,0) 75%)}
.logo{left:80px;top:22px;display:flex;align-items:center;gap:8px;color:var(--white);font-size:20px;font-weight:500}
.logo-mark{width:24px;height:24px;border-radius:50%;background:var(--white)}
.nav{right:79px;top:29px;display:flex;gap:6px;font-size:9.5px;font-weight:500;color:var(--white)}
.nav .on{color:var(--green)}
.nav .sep{color:#ccc}
.hero-title{left:378px;top:102px;font-family:"Arimo",sans-serif;font-size:35px;color:var(--green);font-weight:400}
.hero-sub{left:380px;top:161px;font-family:"Arimo",sans-serif;font-size:13.5px;color:var(--white)}
.hero-text{left:380px;top:196px;width:300px;font-family:"Arimo",sans-serif;font-size:8.8px;line-height:17px;color:#d6d6d6}
.hero-btn{left:537px;top:252px;width:129px;height:33px;background:var(--green);border:2px solid var(--green-dark);box-shadow:0 2px 5px rgba(0,0,0,.5);font-family:"Arimo",sans-serif;font-weight:700;font-size:15px;color:var(--dark);display:flex;align-items:center;justify-content:center}
.section-title{left:0;width:759px;text-align:center;font-family:"Arimo",sans-serif;font-size:18px;color:var(--ink)}
.section-title .g{color:var(--green)}
.welcome-text{left:80px;top:400px;width:600px;text-align:center;font-size:8.8px;line-height:17px;color:var(--text)}
.card{top:492px;width:187px;height:110px}
.card-text{left:79px;background:#2e3336;color:var(--white);text-align:center;padding-top:17px}
.card-text h3{font-family:"Arimo",sans-serif;font-weight:400;font-size:12.5px;color:var(--green);margin-bottom:9px}
.card-text p{font-size:8.8px;line-height:17px}
.card-text em{display:block;margin-top:5px;font-family:"Arimo",sans-serif;font-size:9.5px;color:var(--green)}
.card-shop{left:287px;background:linear-gradient(135deg,#3b6c7e,#9cc94a 55%,#e7c93a)}
.card-device{left:494px;background:linear-gradient(135deg,#c9c9c9,#5a5a5a 60%,#3d3d3d)}
.chat{left:621px;top:500px;width:132px;height:49px;background:var(--green);display:flex;align-items:center}
.chat-icon{width:41px;height:49px;background:var(--green-dark);display:flex;align-items:center;justify-content:center}
.chat-icon span{width:18px;height:18px;border-radius:50%;background:var(--white)}
.chat-label{margin-left:8px;font-size:11px;color:var(--white);flex:1}
.chat-plus{width:16px;height:16px;margin-right:9px;background:var(--white);color:var(--green);font-weight:700;font-size:13px;line-height:16px;text-align:center}
.video{left:79px;top:622px;width:301px;height:210px;background:linear-gradient(120deg,#3d3f3b,#5a5c55 50%,#2f3130)}
.play{left:204px;top:702px}
.video-copy{left:380px;top:622px;width:300px;height:210px;background:var(--green);padding:26px 18px 0 17px;color:var(--white)}
.video-copy .lead{font-family:"Roboto Condensed",sans-serif;font-weight:300;font-size:15px;line-height:21px}
.video-copy .small{margin-top:13px;font-size:8.8px;font-weight:500;line-height:17px}
.dots{margin-top:26px;display:flex;gap:11px}
.dots i{width:7px;height:7px;border-radius:50%;background:#3f7a17}
.dots i:first-child{background:var(--white)}
.testi{left:0;top:852px;width:759px;height:163px;background:linear-gradient(90deg,#23292b,#363b3a 50%,#2a2f31)}
.testi-title{left:80px;top:866px;font-family:"Arimo",sans-serif;font-size:18px;color:var(--green)}
.testi-photo{left:79px;top:907px;width:79px;height:72px;background:linear-gradient(160deg,#c8d8e4,#e6c8a8 60%,#a98f70)}
.quote-mark{font-family:"Arimo",sans-serif;font-size:34px;font-weight:700;color:#6c7070;line-height:1}
.testi-text{left:204px;top:911px;width:344px;font-size:8.8px;line-height:17px;color:#d8d8d8}
.testi-rule{left:566px;top:907px;width:1px;height:72px;background:#777}
.testi-name{left:582px;top:928px;font-size:9.5px;color:var(--green)}
.testi-role{left:582px;top:946px;font-size:8.5px;font-style:italic;color:var(--white)}
.footer{left:0;top:1015px;width:759px;height:149px;background:var(--footer)}
.foot-head{font-size:10.5px;font-weight:500;color:var(--ink);padding-bottom:6px;border-bottom:3px solid #cfcfcf}
.info{left:79px;top:1030px;width:104px}
.info ul{list-style:none;margin-top:8px}
.info li{font-size:8px;line-height:15.7px;color:#555}
.quote{left:272px;top:1030px;width:408px}
.contact{left:272px;top:1058px;width:120px;font-size:7.5px;color:#555;line-height:10px}
.contact b{display:block;font-family:"Arimo",sans-serif;font-style:italic;font-weight:400;font-size:9.5px;color:var(--ink);margin-top:3px}
.field{background:var(--white);border:1px solid #d5d5d5;font-size:7.5px;font-style:italic;color:#999;padding:4px 6px}
.submit{left:626px;top:1134px;width:54px;height:19px;background:var(--green);color:var(--ink);font-size:10px;font-weight:500;display:flex;align-items:center;justify-content:center}
.bar{left:0;top:1164px;width:759px;height:36px;background:var(--bar)}
.copy{left:79px;top:1177px;font-size:7.5px;color:#aaa}
.social{left:546px;top:1171px;display:flex;gap:8px}
.social span{width:21px;height:21px;border-radius:50%;border:1.5px solid #777}
.social span:first-child{background:#3b5a9a;border-color:#3b5a9a}
</style>
</head>
<body>
<div class="abs hero"></div>
<div class="abs hero-photo" role="img" aria-label="Hand holding a smartphone showing the site on its screen"></div>
<div class="abs logo"><span class="logo-mark"></span>vorlisk</div>
<nav class="abs nav">
  <span class="on">Home</span><span class="sep">/</span><span>Who We Are</span><span class="sep">/</span><span>What We Do</span><span class="sep">/</span><span>Services</span><span class="sep">/</span><span>Case Studies</span><span class="sep">/</span><span>Blog</span><span class="sep">/</span><span>Reach Us</span>
</nav>
<h1 class="abs hero-title">Lorem ipsum dolor</h1>
<p class="abs hero-sub">Consectetur adipiscing adipiscing leo pretium</p>
<p class="abs hero-text">Etiam pulvinar ligula tortor, et dsim magna lobortis ut Fusce leo mauris, Coulputate quis nisi sit ametluctus mi.</p>
<div class="abs hero-btn">Case Studies</div>

<h2 class="abs section-title" style="top:371px"><span class="g">Welcome to</span> Vorlisk</h2>
<p class="abs welcome-text">Lorem ipsum dolor sit amet, consectetur adipiscing elit. Praesent adipiscing leo a venenatis pretium. Etiam pulvinar ligula tortor, et dignissim magna lobortis ut. Fusce leo mauris, vulputate quis nisi sit amet, hendrerit luctus mi. Sed auctor neque metus, in dictum neque semper scelerisque. Etiam lacinia sem sit amet mauris euismod rhoncus. Morbi sed dui id ante eleifend fringilla id id est. Nam quis pulvinar tortor, quis ultricies ligula.</p>

<h2 class="abs section-title" style="top:460px">Case <span class="g">Studies</span></h2>
<div class="abs card card-text">
  <h3>Lorem ipsum dolor sit amet</h3>
  <p>Lorem ipsum dolor sit consectetur<br>adipiscing elituis nisi sit amet.</p>
  <em>View case study</em>
</div>
<div class="abs card card-shop" role="img" aria-label="Woman holding a pink smartphone and shopping bags"></div>
<div class="abs card card-device" role="img" aria-label="Tablet on a desk beside a keyboard and earphones"></div>
<div class="abs chat"><div class="chat-icon"><span></span></div><div class="chat-label">Live chat</div><div class="chat-plus">+</div></div>

<div class="abs video" role="img" aria-label="Two colleagues working together at a computer"></div>
<svg class="abs play" width="52" height="52" viewBox="0 0 52 52" aria-hidden="true"><circle cx="26" cy="26" r="24" fill="none" stroke="#7cbf43" stroke-width="3"/><path d="M20 15 L37 26 L20 37 Z" fill="#7cbf43"/></svg>
<div class="abs video-copy">
  <p class="lead">Lorem ipsum dolor sit amet, conseetur adipiscing elit. Sed non rutrum risavnon suslormcipit mauris. Donec feugiat leo quloreis ante venenatis, facilisis tincidunt est laoreet.</p>
  <p class="small">Lorem ipsum dolor sit amet, consectetur adipiscing elit. Sed non rutrum risus, non suscipit mauris.</p>
  <div class="dots"><i></i><i></i><i></i><i></i></div>
</div>

<div class="abs testi"></div>
<h2 class="abs testi-title">Testimonials</h2>
<div class="abs testi-photo" role="img" aria-label="Smiling customer on the phone"></div>
<span class="abs quote-mark" style="left:177px;top:904px">&ldquo;</span>
<p class="abs testi-text">Lorem ipsum dolor sit amet, consectr adipiscing elit. Cras porta arcu nec orcaccumsan tempus. Etiam rit gravida ligula sed condimentum. Ndio erat, lobortis sit amet commodo lorem ispumac, iaculis sit amet nibh. Aenean dapibus erat auod mollis ut ac purumpus. Etiam rit gravida ligula sed condi</p>
<span class="abs quote-mark" style="left:358px;top:960px">&rdquo;</span>
<div class="abs testi-rule"></div>
<p class="abs testi-name">Lorem ispum dolor</p>
<p class="abs testi-role">Senior Director</p>

<div class="abs footer"></div>
<div class="abs info">
  <h3 class="foot-head">Information</h3>
  <ul><li>Home</li><li>Who We Are</li><li>What We Do</li><li>Services</li><li>Our Work / Case Studies</li><li>Reach Us</li></ul>
</div>
<div class="abs quote"><h3 class="foot-head">Get a Quote</h3></div>
<div class="abs contact">
  <b>Address:</b>8901 Lorem ispum dolor<br>25, street 023145, Site amet
  <b>Telephone:</b>+91 123 456 7890
  <b>E-mail:</b>info@vorlisk.com
</div>
<div class="abs field" style="left:404px;top:1059px;width:132px;height:19px">Name</div>
<div class="abs field" style="left:548px;top:1059px;width:132px;height:19px">Email</div>
<div class="abs field" style="left:404px;top:1087px;width:276px;height:37px">Message</div>
<div class="abs submit">Submit</div>

<div class="abs bar"></div>
<p class="abs copy">&copy; Copyright 2014 Vorlisk. All rights reserved.</p>
<div class="abs social"><span></span><span></span><span></span><span></span><span></span></div>
</body>
</html>
```